Web form face-lift for an online startup

We are a web startup building a SaaS application for the Cargolane. The project is mainly dedicated to the paint the main form that our customer are using along the search results that the they get. All details are in the attached documents.
Updates
The application serves the Freight Forwarders community so please think towards this industry when using background images, banners, colors, icons, etc. Computer and technology images are irrelevant.
Customer fields at the top of the page is actually part of the form.
Target Market(s)
Usually business users (Sales people, procurement, shippers, freight forwarders). Some are less tech savvy and some appreciate the new trendy web apps.
Industry/Entity Type
Building
Colors
Designer to choose colors to be used in the design.
Look and feel
Each slider illustrates characteristics of the customer's brand and the style your logo design should communicate.

```html
<!DOCTYPE html>
<html lang="en">
<head>
<meta charset="utf-8">
<title>Cargolane – Search for Quotes</title>
<link href="https://fonts.googleapis.com/css2?family=Nunito:wght@300;400;600;700;800&display=swap" rel="stylesheet">
<style>
:root{
  --topbar:#063a3a;
  --header:#0a4d4b;
  --orange:#f58a22;
  --blue:#1a8fdc;
  --blue-dark:#1778c4;
  --page:#f3f1ed;
  --panel:#ffffff;
  --text:#2f2f2f;
  --muted:#8a8a8a;
  --border:#cfcfcf;
  --select:#e9e9e6;
  --red:#e0202a;
}
*{box-sizing:border-box;margin:0;padding:0}
html,body{width:1200px;height:951px;overflow:hidden}
body{font-family:"Nunito",sans-serif;background:var(--page);color:var(--text);position:relative}
.abs{position:absolute}
.topbar{left:0;top:0;width:1200px;height:39px;background:var(--topbar);color:#cfdcdc;font-size:11px}
.topbar span{position:absolute;top:12px}
.caret{display:inline-block;border:3px solid transparent;border-top:4px solid #cfdcdc;margin-left:4px;vertical-align:1px}
.header{left:0;top:39px;width:1200px;height:92px;background:var(--header)}
.brand{left:159px;top:22px;display:flex;align-items:center;gap:12px;color:#fff;font-weight:800;font-size:40px;letter-spacing:1px}
.brand-mark{width:36px;height:36px;border-radius:50%;border:3px solid #fff}
.nav a{position:absolute;top:37px;color:#e6efef;font-size:12px;font-weight:400;letter-spacing:.5px;text-decoration:none}
.btn-top{position:absolute;top:25px;height:36px;width:73px;border-radius:3px;color:#fff;font-size:12px;font-weight:800;display:flex;align-items:center;justify-content:center}
.h1{font-size:28px;font-weight:800;color:var(--orange)}
.label{font-size:13px;font-weight:800}
.field{position:absolute;background:#fff;border:1px solid var(--border);font-size:11px;color:var(--muted);font-weight:700;display:flex;align-items:center;justify-content:center}
.field.left{justify-content:flex-start;padding-left:10px}
.select{position:absolute;background:var(--select);border:1px solid #d3d3d0;font-size:11px;font-weight:700;color:#555;display:flex;align-items:center;padding-left:10px}
.select::after{content:"";position:absolute;right:10px;top:50%;margin-top:-3px;border:5px solid transparent;border-top:6px solid #555}
.checkbox{position:absolute;width:14px;height:14px;border:1px solid #bbb;background:#fff;border-radius:2px}
.tab{position:absolute;top:247px;width:89px;height:46px;background:#f1f1ef;border:1px solid #d6d6d3;display:flex;align-items:center;justify-content:center}
.tab.active{background:#fff}
.panel{left:175px;top:293px;width:851px;height:235px;background:var(--panel)}
.radio{position:absolute;width:15px;height:15px;border:1px solid #aaa;border-radius:50%;background:#fff}
.opt{position:absolute;font-size:14px;font-weight:800}
.search-btn{left:429px;top:758px;width:343px;height:71px;border-radius:4px;background:linear-gradient(#1e95e0,#1679c6);color:#fff;font-size:28px;font-weight:800;display:flex;align-items:center;justify-content:center;letter-spacing:.5px}
.footer{left:0;top:883px;width:1200px;height:68px;background:#fff}
.footer a{position:absolute;top:28px;font-size:13px;color:#666;text-decoration:none;letter-spacing:.5px}
.social{position:absolute;top:15px;width:40px;height:40px;border-radius:50%}
</style>
</head>
<body>

<div class="abs topbar">
  <span style="left:894px">USD<i class="caret"></i></span>
  <span style="left:943px;top:10px">
    <svg width="22" height="18" viewBox="0 0 22 18" aria-hidden="true"><rect width="22" height="18" fill="#1f3a8a"/><path d="M0 0L22 18M22 0L0 18" stroke="#fff" stroke-width="3"/><path d="M11 0V18M0 9H22" stroke="#fff" stroke-width="5"/><path d="M11 0V18M0 9H22" stroke="#d22" stroke-width="2.5"/></svg><i class="caret"></i>
  </span>
  <span style="left:988px;top:7px">
    <svg width="25" height="25" viewBox="0 0 25 25" aria-hidden="true"><circle cx="12.5" cy="12.5" r="11.5" fill="none" stroke="#cfdcdc" stroke-width="1.5"/><circle cx="12.5" cy="10" r="4" fill="#cfdcdc"/><path d="M5 20c2-4 13-4 15 0" fill="#cfdcdc"/></svg>
  </span>
  <span style="left:1016px"><i class="caret" style="margin:0 3px 0 0"></i>USERNAME</span>
</div>

<header class="abs header">
  <div class="abs brand"><span class="brand-mark"></span>CARGOLANE</div>
  <nav class="nav">
    <a style="left:553px">SOLUTIONS</a>
    <a style="left:667px">CUSTOMERS</a>
    <a style="left:779px">BLOG</a>
    <a style="left:851px">CONTACT US</a>
  </nav>
  <div class="btn-top" style="left:956px;background:var(--orange)">LOG IN</div>
  <div class="btn-top" style="left:1039px;background:var(--blue)">SIGN UP</div>
</header>

<h1 class="abs h1" style="left:174px;top:148px">Search for Quotes</h1>

<div class="abs label" style="left:174px;top:205px">Customer</div>
<div class="field" style="left:255px;top:197px;width:325px;height:35px"></div>

<div class="checkbox" style="left:175px;top:257px"></div>
<div class="abs label" style="left:203px;top:254px;font-size:14px">Rate quote</div>
<svg class="abs" style="left:296px;top:252px" width="122" height="24" viewBox="0 0 122 24" aria-label="3 of 5 stars">
  <defs><polygon id="star" points="12,1 15,8.5 23,9 17,14 19,22 12,17.8 5,22 7,14 1,9 9,8.5"/></defs>
  <use href="#star" x="0" fill="#1a8fdc"/><use href="#star" x="24.5" fill="#1a8fdc"/><use href="#star" x="49" fill="#1a8fdc"/>
  <use href="#star" x="73.5" fill="none" stroke="#1a8fdc" stroke-width="1.2"/><use href="#star" x="98" fill="none" stroke="#1a8fdc" stroke-width="1.2"/>
</svg>

<div class="tab active" style="left:682px">
  <svg width="40" height="32" viewBox="0 0 40 32" aria-label="Pallet cargo"><path d="M4 4h5l6 20h20" fill="none" stroke="#1a8fdc" stroke-width="2.5"/><rect x="15" y="8" width="16" height="13" fill="#1a8fdc" transform="rotate(-8 23 14)"/><circle cx="15" cy="27" r="3" fill="none" stroke="#1a8fdc" stroke-width="2"/></svg>
</div>
<div class="tab" style="left:777px">
  <svg width="46" height="32" viewBox="0 0 46 32" aria-label="Road freight"><rect x="8" y="6" width="22" height="16" fill="#9a9a9a"/><path d="M30 10h7l5 6v6H30z" fill="#9a9a9a"/><circle cx="15" cy="24" r="3.5" fill="#f1f1ef" stroke="#9a9a9a" stroke-width="2"/><circle cx="35" cy="24" r="3.5" fill="#f1f1ef" stroke="#9a9a9a" stroke-width="2"/><path d="M0 10h6M2 14h4M0 18h6" stroke="#9a9a9a" stroke-width="1.5"/></svg>
</div>
<div class="tab" style="left:871px">
  <svg width="46" height="28" viewBox="0 0 46 28" aria-label="Courier"><rect x="14" y="4" width="28" height="19" fill="#9a9a9a"/><path d="M14 4l14 11 14-11" fill="none" stroke="#f1f1ef" stroke-width="2"/><path d="M2 10h9M5 14h6M2 18h9" stroke="#9a9a9a" stroke-width="1.5"/></svg>
</div>
<div class="abs label" style="left:979px;top:263px;font-size:13px">more &gt;</div>

<section class="abs panel"></section>
<div class="abs label" style="left:197px;top:320px">Qty</div>
<div class="abs label" style="left:262px;top:320px">Stackabel</div>
<div class="abs label" style="left:348px;top:320px">Load</div>
<div class="abs label" style="left:578px;top:320px">Length</div>
<div class="abs label" style="left:651px;top:320px">Width</div>
<div class="abs label" style="left:722px;top:320px">Height</div>
<div class="abs label" style="left:867px;top:320px">Weight</div>

<div class="field left" style="left:197px;top:351px;width:61px;height:35px">5</div>
<div class="checkbox" style="left:288px;top:361px"></div>
<div class="select" style="left:349px;top:351px;width:219px;height:35px;padding-left:18px;color:#888">Box /Pallet</div>
<div class="field" style="left:579px;top:351px;width:61px;height:35px">100</div>
<div class="field" style="left:651px;top:351px;width:61px;height:35px">100</div>
<div class="field" style="left:723px;top:351px;width:61px;height:35px">100</div>
<div class="select" style="left:795px;top:351px;width:62px;height:35px">cm</div>
<div class="field" style="left:867px;top:351px;width:62px;height:35px">100</div>
<div class="select" style="left:939px;top:351px;width:62px;height:35px;padding-left:16px">kg</div>

<div class="abs" style="left:197px;top:403px;width:153px;height:35px;background:var(--orange);border-radius:2px;color:#fff;font-size:13px;font-weight:800;display:flex;align-items:center;padding-left:12px;gap:14px">
  <svg width="14" height="14" viewBox="0 0 14 14" aria-hidden="true"><path d="M7 0v14M0 7h14" stroke="#fff" stroke-width="2.5"/></svg>Add more units
</div>

<div class="abs" style="left:197px;top:454px;width:804px;height:1px;background:#e3e3e3"></div>

<div class="abs label" style="left:610px;top:484px;color:var(--blue);font-size:14px">Total</div>
<div class="field left" style="left:651px;top:475px;width:61px;height:35px">5</div>
<div class="field left" style="left:723px;top:474px;width:61px;height:35px">100</div>
<div class="select" style="left:795px;top:474px;width:62px;height:35px">CBM</div>
<div class="field left" style="left:867px;top:474px;width:62px;height:35px">1</div>
<div class="select" style="left:939px;top:474px;width:62px;height:35px;padding-left:16px">kg</div>

<div class="abs label" style="left:177px;top:558px;font-size:14px">From</div>
<div class="field left" style="left:239px;top:549px;width:288px;height:35px;color:var(--text);font-size:13px">Shipping address or port</div>
<svg class="abs" style="left:604px;top:558px" width="21" height="17" viewBox="0 0 21 17" aria-hidden="true"><path d="M0 5h11V0l10 8.5L11 17v-5H0z" fill="#b5b5b5"/></svg>
<div class="abs label" style="left:703px;top:558px;font-size:14px">To</div>
<div class="field left" style="left:738px;top:549px;width:288px;height:35px;color:var(--text);font-size:13px;padding-left:17px">Shipping address or port</div>

<h2 class="abs h1" style="left:174px;top:610px">Options</h2>

<div class="radio" style="left:174px;top:676px"></div><div class="opt" style="left:200px;top:673px">Import</div>
<div class="radio" style="left:271px;top:676px"></div><div class="opt" style="left:303px;top:673px">Export</div>
<div class="radio" style="left:372px;top:677px"></div><div class="opt" style="left:397px;top:675px">Incoterm: FCA</div>

<svg class="abs" style="left:556px;top:661px" width="134" height="36" viewBox="0 0 134 36" aria-label="Excluded cargo types">
  <g fill="#fff" stroke="#e0202a" stroke-width="3">
    <circle cx="17" cy="18" r="15"/><circle cx="67" cy="18" r="15"/><circle cx="115" cy="18" r="15"/>
  </g>
  <g fill="#8a8a8a">
    <path d="M11 11l6-3 6 3v6c0 5-6 8-6 8s-6-3-6-8z"/>
    <ellipse cx="67" cy="18" rx="8" ry="5"/>
    <circle cx="115" cy="18" r="7"/>
  </g>
  <path d="M7 8l20 20M57 8l20 20M105 8l20 20" stroke="#e0202a" stroke-width="3"/>
</svg>

<div class="select" style="left:738px;top:660px;width:288px;height:35px;padding-left:16px;font-size:14px;font-weight:800;color:var(--text)">Price level</div>
<div class="abs" style="left:934px;top:709px;font-size:11px;font-weight:800;color:var(--blue);text-decoration:underline;letter-spacing:.3px">MORE OPTIONS</div>

<div class="abs search-btn">Search quotes</div>
<div class="abs" style="left:523px;top:835px;font-size:17px;color:#555;text-decoration:underline;letter-spacing:.5px">or create manually</div>

<footer class="abs footer">
  <a style="left:174px">ABOUT US</a>
  <a style="left:277px">PRIVACY POLICY</a>
  <a style="left:411px">TERMS OF SERVICE</a>
  <a style="left:566px">NEWS</a>
  <div class="social" role="img" aria-label="Professional network" style="left:785px;background:#0f66b8"></div>
  <div class="social" role="img" aria-label="Video channel" style="left:835px;background:#d9342b"></div>
  <div class="social" role="img" aria-label="Share" style="left:885px;background:#f07d32"></div>
  <div class="social" role="img" aria-label="Microblog" style="left:935px;background:#2aa4e0"></div>
  <div class="social" role="img" aria-label="Social network" style="left:986px;background:#3a5898"></div>
</footer>

</body>
</html>
```